Create for us a Shop-Stopper Business Card

We need a standout, first class business card to go along with our new brand strategy. Sleek, Contemporary and fresh.

Colors and theme must sync with our websitewww.pelvorpower.co.uk

We want a business card that has a global brand appeal. TKR Energy is a small UK renewable company that specialises in energy projects in Africa. We want a business card that has the following characteristics: Very short, precise, global, stand out, NOT TOO LOUD but contemporary. The company's colour themes are White, Grey with a hint of green.

Target Market(s)

Business exec, high net worth individuals, investors, commercial leaders, suppliers, government officials

Industry/Entity Type

Solar Energy

Contact Information for Business Card

Logo, Name, Title, Address, web address, email,

Requirements
Must have
• Logo must be sharp
Nice to have
• Adapt fonts from the logo. The large circular side of the logo at the back in a very refreshing way
Should not have
• No solar panel shapes or image.Very little black. If possible avoid black. Its not coming out nice. I think !!!

```html
<!DOCTYPE html>
<html lang="en">
<head>
<meta charset="utf-8">
<title>TKR Energy Business Card</title>
<link href="https://fonts.googleapis.com/css2?family=Open+Sans:wght@400;600;700&display=swap" rel="stylesheet">
<style>
  :root {
    --page: #e9e7e3;
    --card-white: #ffffff;
    --ink: #333333;
    --ink-soft: #4a4a4a;
    --green: #1e7a34;
    --green-light: #8cc63f;
    --grey-band: #5a5a5a;
    --grey-band-dark: #3c3c3c;
    --rule: #cfcfcf;
    --accent-red: #d9322b;
    --back-dark: #3f3f3f;
    --back-mid: #5e5e5e;
    --faint-ring: rgba(0,0,0,0.04);
  }
  * { margin: 0; padding: 0; box-sizing: border-box; }
  html, body { width: 1200px; height: 1000px; overflow: hidden; }
  body { background: var(--page); font-family: "Open Sans", sans-serif; position: relative; }

  .card { position: absolute; left: 265px; width: 666px; height: 397px; overflow: hidden; box-shadow: 0 4px 14px rgba(0,0,0,0.18); }
  .card--front { top: 73px; background: var(--card-white); }
  .card--back { top: 532px; background: radial-gradient(circle at 165px 175px, var(--back-mid) 0%, var(--back-dark) 55%, #393939 100%); }

  .deco-ring { position: absolute; left: 40px; top: 20px; width: 310px; height: 310px; border-radius: 50%; border: 34px solid var(--faint-ring); }
  .card--back .deco-ring { border-color: rgba(255,255,255,0.06); }

  .brand { position: absolute; display: flex; align-items: center; gap: 10px; }
  .brand__dot { width: 62px; height: 62px; border-radius: 50%; background: var(--green); flex: none; }
  .brand__name { font-weight: 600; font-size: 40px; letter-spacing: 1px; color: var(--ink); padding-bottom: 4px; border-bottom: 2px solid var(--accent-red); line-height: 1.1; }
  .card--front .brand { right: 32px; top: 64px; }

  .card--back .brand { right: 32px; bottom: 48px; }
  .card--back .brand__dot { width: 54px; height: 54px; background: #ffffff; }
  .card--back .brand__name { color: #ffffff; font-size: 34px; border-bottom-color: #ffffff; }

  .person { position: absolute; left: 33px; top: 197px; }
  .person__name { font-weight: 700; font-size: 21px; line-height: 28px; color: var(--green); letter-spacing: 0.2px; }
  .person__title { font-size: 16px; line-height: 22px; color: var(--ink-soft); }

  .divider { position: absolute; left: 33px; width: 452px; top: 260px; height: 1px; background: var(--rule); }

  .address { position: absolute; left: 33px; top: 287px; font-size: 16px; line-height: 21px; color: var(--ink-soft); font-style: normal; }

  .contacts { position: absolute; right: 32px; top: 249px; list-style: none; text-align: right; font-size: 16px; line-height: 24px; color: var(--ink-soft); }
  .contacts li { display: flex; justify-content: flex-end; align-items: center; gap: 7px; }
  .contacts svg { width: 13px; height: 13px; fill: var(--green); flex: none; }

  .band { position: absolute; left: 0; bottom: 0; width: 100%; height: 28px; }
</style>
</head>
<body>

<section class="card card--front" aria-label="Business card front">
  <div class="deco-ring" aria-hidden="true"></div>

  <div class="brand">
    <span class="brand__dot" aria-hidden="true"></span>
    <span class="brand__name">TKR ENERGY</span>
  </div>

  <div class="person">
    <p class="person__name">DANIEL ASHWORTH</p>
    <p class="person__title">Managing Director</p>
  </div>

  <div class="divider"></div>

  <address class="address">
    Level 14, 8 Harbour Court<br>
    Brisbane, 40, Queensland
  </address>

  <ul class="contacts">
    <li>+ 000 000 0000
      <svg viewBox="0 0 12 16" aria-hidden="true"><path d="M2 0h8a1 1 0 0 1 1 1v14a1 1 0 0 1-1 1H2a1 1 0 0 1-1-1V1a1 1 0 0 1 1-1zm1 2v7h6V2zm0 9v1h2v-1zm4 0v1h2v-1zm-4 2v1h2v-1zm4 0v1h2v-1z"/></svg>
    </li>
    <li>+ 000 000 0000
      <svg viewBox="0 0 16 14" aria-hidden="true"><path d="M1 4c0-2 3-3 7-3s7 1 7 3v1h-4V3.5H5V5H1zm3 2h8l2 7H2z"/></svg>
    </li>
    <li>info@pelvorpower.co.uk
      <svg viewBox="0 0 16 12" aria-hidden="true"><path d="M0 0h16v12H0zm1 1.5V2l7 5 7-5v-.5z"/></svg>
    </li>
    <li>www.tkrgroupltd.com
      <svg viewBox="0 0 16 16" aria-hidden="true"><circle cx="8" cy="8" r="7.5"/><path d="M0.5 8h15M8 0.5v15" stroke="#fff" stroke-width="1.2"/></svg>
    </li>
  </ul>

  <svg class="band" viewBox="0 0 666 28" preserveAspectRatio="none" aria-hidden="true">
    <defs>
      <linearGradient id="bandGreen" x1="0" x2="1">
        <stop offset="0" stop-color="#1e7a34"/>
        <stop offset="1" stop-color="#8cc63f"/>
      </linearGradient>
      <linearGradient id="bandGrey" x1="0" x2="1">
        <stop offset="0" stop-color="#3c3c3c"/>
        <stop offset="1" stop-color="#5a5a5a"/>
      </linearGradient>
    </defs>
    <polygon points="0,12 322,12 332,28 0,28" fill="url(#bandGreen)"/>
    <polygon points="326,28 345,0 666,0 666,28" fill="url(#bandGrey)"/>
    <polygon points="322,28 342,0 346,0 327,28" fill="#ffffff"/>
  </svg>
</section>

<section class="card card--back" aria-label="Business card back">
  <div class="deco-ring" aria-hidden="true"></div>
  <div class="brand">
    <span class="brand__dot" aria-hidden="true"></span>
    <span class="brand__name">TKR ENERGY</span>
  </div>
</section>

</body>
</html>
```